Crooked Thrill

I would like a website that does e-commerce and able to take payments for merchandise and orders.

Target Market(s)

Skate, BMX, surf, drink, adventure, motorcycle, rock n roll, bars, hot rods, tattoos, rebels

Industry/Entity Type

Brand market

Coding

Coded - Design and coding required

Number of Pages Required

1 page

Font styles to use
Serif

Requirements
Must have
• E-commerce
Nice to have
• Pictures of merch on people... Ex. People wearing our hats

```html
<!DOCTYPE html>
<html lang="en">
<head>
<meta charset="utf-8">
<title>Crooked Thrill</title>
<link href="https://fonts.googleapis.com/css2?family=Bebas+Neue&family=Poppins:ital,wght@0,400;0,500;0,600;1,400&display=swap" rel="stylesheet">
<style>
:root{
  --gold:#dfc77a;
  --gold-text:#d6b862;
  --ink:#1f1f1f;
  --muted:#555;
  --line:#e2e2e2;
  --white:#fff;
  --sky:#d8e5ea;
  --fog:#e4e4e4;
  --charcoal:#414141;
  --footer:#f2f2f2;
}
*{box-sizing:border-box;margin:0;padding:0}
html,body{width:1200px;height:4717px;overflow:hidden}
body{position:relative;background:var(--white);font-family:"Poppins",sans-serif;color:var(--ink)}
.abs{position:absolute}
.display{font-family:"Bebas Neue",sans-serif;font-weight:400;letter-spacing:1px}
.section-title{position:absolute;left:0;width:1200px;text-align:center;font-family:"Bebas Neue",sans-serif;font-size:48px;line-height:1;color:#2a2a2a}

/* header */
.site-header{position:absolute;left:0;top:0;width:1200px;height:143px;background:var(--white);z-index:3}
.brand-name{position:absolute;left:106px;top:52px;font-family:"Poppins",sans-serif;font-weight:600;font-size:28px;line-height:36px;color:#333;white-space:nowrap}
.search{position:absolute;left:641px;top:26px;width:334px;height:44px;border:1.5px solid #bbb;border-radius:22px;font-size:13px;color:#999;padding:12px 20px}
.search svg{position:absolute;right:16px;top:12px}
.login{position:absolute;left:1004px;top:38px;font-size:14px;font-weight:500;display:flex;gap:6px;align-items:center}
.cart{position:absolute;left:1093px;top:36px}
.cart-count{position:absolute;left:1110px;top:28px;width:14px;height:14px;border-radius:50%;background:var(--gold);font-size:9px;text-align:center;line-height:14px}
.main-nav{position:absolute;top:102px;left:399px;display:flex;font-size:14px;font-weight:500}
.main-nav a{color:var(--ink);text-decoration:none;margin-right:36px}

/* hero */
.hero{position:absolute;left:0;top:143px;width:1200px;height:570px;background:linear-gradient(90deg,#5d5d5d,#4a4a4a 55%,#3f3f3f)}
.hero-figure{position:absolute;left:640px;top:58px;width:270px;height:512px;background:linear-gradient(180deg,#3a3a3a,#262626);border-radius:120px 120px 0 0}
.hero-title{position:absolute;left:128px;top:174px;font-family:"Bebas Neue",sans-serif;font-weight:400;font-size:78px;line-height:1;color:var(--white);letter-spacing:2px}
.hero-sub{position:absolute;left:128px;top:245px;font-size:28px;color:var(--white)}
.btn-gold{position:absolute;background:var(--gold);border-radius:30px;font-weight:600;font-size:16px;color:#3a3220;text-align:center}
.hero .btn-gold{left:128px;top:297px;width:277px;height:56px;line-height:56px}

/* product cards */
.product-card{position:absolute;width:224px;height:361px;background:var(--white);border:1.5px solid var(--line);box-shadow:0 1px 4px rgba(0,0,0,.05);text-align:center}
.product-photo{position:absolute;left:22px;top:22px;width:180px;height:170px;border-radius:6px}
.price{position:absolute;left:0;width:100%;top:200px;font-size:21px;font-weight:600;color:var(--gold-text)}
.product-name{position:absolute;left:0;width:100%;top:240px;font-size:15px;line-height:19px;color:var(--muted)}
.add-cart{position:absolute;left:41px;top:296px;width:142px;height:41px;border:2px solid #333;border-radius:21px;font-size:13px;font-weight:600;line-height:37px}

/* popular */
.popular{position:absolute;left:0;top:1352px;width:1200px;height:680px;background:var(--fog)}
.popular-sky{position:absolute;left:0;top:0;width:987px;height:680px;background:var(--sky)}
.popular-model{position:absolute;left:64px;top:95px;width:537px;height:585px;background:linear-gradient(180deg,#d8c39a 0%,#b79a6a 45%,#23283a 75%);border-radius:240px 240px 0 0}

/* deals */
.deal-card{position:absolute;top:2228px;width:292px;height:373px;background:var(--white);box-shadow:0 2px 12px rgba(0,0,0,.09);text-align:center}
.deal-photo{height:205px}
.deal-title{margin-top:38px;font-size:17px;font-weight:600;line-height:24px}
.deal-text{margin-top:12px;font-size:14px;line-height:18px}

/* categories */
.categories{position:absolute;left:0;top:2713px;width:1200px;height:532px;background:var(--fog)}
.cat-card{position:absolute;top:169px;width:209px;height:247px;background:var(--white);text-align:center}
.cat-photo{position:absolute;left:40px;top:26px;width:128px;height:128px;border-radius:50%}
.cat-name{position:absolute;left:0;width:100%;top:186px;font-size:15px;font-weight:600}

/* story */
.story-title{position:absolute;left:121px;top:3386px;font-size:42px;font-weight:500;line-height:48px;color:#222}
.story-text{position:absolute;left:127px;top:3545px;width:440px;font-size:16px;line-height:20px;color:#333}
.story-photo{position:absolute;left:655px;top:3344px;width:412px;height:412px;border-radius:50%;background:radial-gradient(circle at 50% 45%,#e8d0b0 0,#c99a7a 35%,#6b7a4e 70%,#3e4a2f 100%)}

/* testimonials */
.testimonials{position:absolute;left:0;top:3833px;width:1200px;height:458px;background:linear-gradient(180deg,#4a4a4a,#3a3a3a);border-bottom:3px solid var(--gold)}
.testimonials .section-title{top:72px;color:var(--white)}
.quote{position:absolute;top:150px;width:414px;height:234px;padding:38px 28px 0 28px}
.quote.filled{left:147px;background:var(--gold);color:#2b2616}
.quote.outline{left:581px;border:2px solid #cfcfcf;color:var(--white)}
.stars{font-size:22px;letter-spacing:2px;line-height:1}
.quote.outline .stars{color:var(--gold)}
.quote p{margin-top:20px;font-size:15px;font-style:italic;line-height:22px}
.quote .author{margin-top:22px;font-weight:600;font-size:16px}

/* footer */
.site-footer{position:absolute;left:0;top:4294px;width:1200px;height:423px;background:var(--footer)}
.footer-brand{position:absolute;left:118px;top:100px;font-family:"Poppins",sans-serif;font-weight:600;font-size:28px;line-height:36px;color:#333;white-space:nowrap}
.social{position:absolute;top:205px;width:22px;height:22px;border-radius:50%;background:#222}
.footer-col{position:absolute;top:66px}
.footer-col h4{font-family:"Bebas Neue",sans-serif;font-weight:400;font-size:25px;letter-spacing:.5px;margin-bottom:20px}
.footer-col li{list-style:none;font-size:14px;color:#444;line-height:30px}
.newsletter p{font-size:14px;line-height:18px;color:#444;width:280px}
.news-input{margin-top:24px;width:274px;height:42px;border:1px solid #ddd;border-radius:21px;background:var(--white);font-size:13px;color:#999;padding:11px 18px}
.news-btn{margin-top:10px;width:274px;height:46px;border-radius:23px;background:var(--gold);text-align:center;line-height:46px;font-weight:600;font-size:16px}
.footer-rule{position:absolute;left:121px;top:345px;width:978px;height:1px;background:#aaa}
.copyright{position:absolute;left:0;width:1200px;top:370px;text-align:center;font-size:14px;color:#333}
</style>
</head>
<body>

<header class="site-header">
  <div class="brand-name">Crooked Thrill</div>
  <div class="search">Enter Keyword
    <svg width="18" height="18" viewBox="0 0 18 18"><circle cx="7.5" cy="7.5" r="5.5" fill="none" stroke="#333" stroke-width="2"/><line x1="11.5" y1="11.5" x2="16" y2="16" stroke="#333" stroke-width="2.4" stroke-linecap="round"/></svg>
  </div>
  <div class="login">
    <svg width="16" height="17" viewBox="0 0 16 17"><circle cx="8" cy="5" r="4" fill="#333"/><path d="M0 17c0-5 3.5-7 8-7s8 2 8 7z" fill="#333"/></svg>
    LOGIN
  </div>
  <svg class="cart" width="24" height="22" viewBox="0 0 24 22"><path d="M1 2h4l3 12h12l3-9H7" fill="none" stroke="#333" stroke-width="2.2"/><path d="M7 5h15l-2.5 8H9z" fill="#333"/><circle cx="10" cy="19" r="2" fill="#333"/><circle cx="18" cy="19" r="2" fill="#333"/></svg>
  <div class="cart-count">0</div>
  <nav class="main-nav">
    <a>HOME</a><a>SHOP MERCH</a><a>TOP ACCESSORIES</a><a>GIFTS &amp; SETS</a><a>ABOUT US</a><a style="margin-right:0">CONTACT US</a>
  </nav>
</header>

<section class="hero">
  <div class="abs" style="inset:0" role="img" aria-label="Dark stone brick wall background"></div>
  <div class="hero-figure" role="img" aria-label="Man in black cap and black t-shirt looking down"></div>
  <h1 class="hero-title">CROOKED THRILL</h1>
  <p class="hero-sub">Lorem ipsum dolor sit ametcon</p>
  <div class="btn-gold">EXPLORE OUR PRODUCTS</div>
</section>

<h2 class="section-title" style="top:800px">LATEST PRODUCTS</h2>

<div class="product-card" style="left:112px;top:888px">
  <div class="product-photo" role="img" aria-label="Brown cowboy hat" style="background:radial-gradient(ellipse at center,#9a6a3e 0,#c39a72 35%,#fff 70%)"></div>
  <div class="price">$10.50</div><div class="product-name">Product Name Here<br>Lorem Ispsum</div><div class="add-cart">ADD TO CART</div>
</div>
<div class="product-card" style="left:363px;top:888px">
  <div class="product-photo" role="img" aria-label="Black t-shirt" style="background:radial-gradient(ellipse at center,#1a1a1a 0,#333 45%,#fff 72%)"></div>
  <div class="price">$10.50</div><div class="product-name">Product Name Here<br>Lorem Ipsum</div><div class="add-cart">ADD TO CART</div>
</div>
<div class="product-card" style="left:614px;top:888px">
  <div class="product-photo" role="img" aria-label="Silver round keychain" style="background:radial-gradient(circle at 50% 62%,#d6d6d6 0,#b8b8b8 25%,#fff 50%)"></div>
  <div class="price">$10.50</div><div class="product-name">Product Name Here<br>Lorem Ipsum</div><div class="add-cart">ADD TO CART</div>
</div>
<div class="product-card" style="left:863px;top:888px">
  <div class="product-photo" role="img" aria-label="White ceramic mug" style="background:radial-gradient(ellipse at center,#f1f1f1 0,#dedede 35%,#fff 65%)"></div>
  <div class="price">$10.50</div><div class="product-name">Product Name Here<br>Lorem Ipsum</div><div class="add-cart">ADD TO CART</div>
</div>

<section class="popular">
  <div class="popular-sky"></div>
  <div class="popular-model" role="img" aria-label="Woman with long wavy hair wearing a navy cap and black sweatshirt"></div>
  <h2 class="abs display" style="left:685px;top:100px;font-size:46px;color:#2a2a2a">TODAY'S POPULAR PICKS</h2>
  <div class="product-card" style="left:614px;top:178px">
    <div class="product-photo" role="img" aria-label="Black hooded sweatshirt" style="background:radial-gradient(ellipse at center,#1c1c1c 0,#383838 45%,#fff 72%)"></div>
    <div class="price">$10.50</div><div class="product-name">Product Name Here<br>Lorem Ipsum</div><div class="add-cart">ADD TO CART</div>
  </div>
  <div class="product-card" style="left:863px;top:178px">
    <div class="product-photo" role="img" aria-label="Brown cowboy hat" style="background:radial-gradient(ellipse at center,#9a6a3e 0,#c39a72 35%,#fff 70%)"></div>
    <div class="price">$10.50</div><div class="product-name">Product Name Here<br>Lorem Ipsum</div><div class="add-cart">ADD TO CART</div>
  </div>
</section>

<h2 class="section-title" style="top:2127px">HOT DEALS</h2>

<div class="deal-card" style="left:126px">
  <div class="deal-photo" role="img" aria-label="Hands in a knit sweater holding a white mug" style="background:linear-gradient(135deg,#8a8a88,#c9c7c3 50%,#e9e7e4)"></div>
  <div class="deal-title">LOREM IPSUM DOL<br>OR SIT AMET</div>
  <div class="deal-text">Save up to 50% on<br>Lormeuispok</div>
</div>
<div class="deal-card" style="left:454px">
  <div class="deal-photo" role="img" aria-label="Smiling woman in a white t-shirt" style="background:linear-gradient(180deg,#dcdcdc,#cfcfcf 50%,#f3f3f3)"></div>
  <div class="deal-title">LOREM IPSUM DOL<br>OR SIT AMET</div>
  <div class="deal-text">Save up to 50% on<br>Lormeuispok</div>
</div>
<div class="deal-card" style="left:782px">
  <div class="deal-photo" role="img" aria-label="Man adjusting a black cap" style="background:linear-gradient(135deg,#8c8f92,#3a3a3a 50%,#6d5a4c)"></div>
  <div class="deal-title">LOREM IPSUM DOL<br>OR SIT AMET</div>
  <div class="deal-text">Save up to 50% on<br>Lormeuispok</div>
</div>

<section class="categories">
  <h2 class="section-title" style="top:79px">SHOP BY CATEGORY</h2>
  <div class="cat-card" style="left:169px"><div class="cat-photo" role="img" aria-label="Black insulated bottle" style="background:radial-gradient(circle,#3a2e28 0,#6b5a4c 45%,#a68c72 100%)"></div><div class="cat-name">CATEGORY NAME</div></div>
  <div class="cat-card" style="left:396px"><div class="cat-photo" role="img" aria-label="White mug" style="background:radial-gradient(circle,#f4f4f4 0,#dfe3e6 45%,#5a4a40 100%)"></div><div class="cat-name">CATEGORY NAME</div></div>
  <div class="cat-card" style="left:623px"><div class="cat-photo" role="img" aria-label="Person in a brown hat outdoors" style="background:radial-gradient(circle,#6e5a48 0,#9aa2a6 55%,#c9d0d3 100%)"></div><div class="cat-name">CATEGORY NAME</div></div>
  <div class="cat-card" style="left:848px"><div class="cat-photo" role="img" aria-label="Person in a black t-shirt" style="background:radial-gradient(circle,#141414 0,#2a2a2a 50%,#bfbfbf 100%)"></div><div class="cat-name">CATEGORY NAME</div></div>
</section>

<h2 class="story-title">Lorem ipsum dolor<br>sit amet, consectetur<br>adipiscing elit, sed</h2>
<p class="story-text">Lorem ipsum dolor sit amet, consectetur adipiscing elit, sed do eiusmod tempor incididunt ut labore et dolore magna aliqua. Quis ipsum suspendisse ultrices gravida. Risus commod.</p>
<div class="btn-gold" style="left:132px;top:3648px;width:161px;height:49px;line-height:49px">READ MORE</div>
<div class="story-photo" role="img" aria-label="Smiling woman in a white hat among pink flowers"></div>

<section class="testimonials">
  <div class="abs" style="inset:0" role="img" aria-label="Dark brick wall background"></div>
  <h2 class="section-title">CLIENT TESTIMONIALS</h2>
  <div class="quote filled">
    <div class="stars">★★★★★</div>
    <p>Lorem ipsum dolor sit ameconsectetur adipiscing elitse do eiusmod tempordnt ut labore et dolore mag na aliqu orem ipsum dolor sit ameconsectetur adipiscin</p>
    <div class="author">ROBYN J</div>
  </div>
  <div class="quote outline">
    <div class="stars">★★★★★</div>
    <p>Lorem ipsum dolor sit ameconsectetur adipiscing elitse do eiusmod tempordnt ut labore et dolore mag na aliqu orem ipsum dolor sit ameconsectetur adipiscin</p>
    <div class="author">ROBYN J</div>
  </div>
</section>

<footer class="site-footer">
  <div class="footer-brand">Crooked Thrill</div>
  <div class="social" style="left:163px" role="img" aria-label="Social profile"></div>
  <div class="social" style="left:205px" role="img" aria-label="Social profile"></div>
  <div class="social" style="left:245px" role="img" aria-label="Social profile"></div>

  <div class="footer-col" style="left:403px">
    <h4>SERVICE</h4>
    <ul><li>My Account</li><li>Rewards</li><li>Returns</li><li>Shipping Policy</li><li>Corporate Gifting</li><li>FAQs</li></ul>
  </div>
  <div class="footer-col" style="left:605px">
    <h4>ABOUT</h4>
    <ul><li>Our Products</li><li>Contact</li><li>FAQs</li><li>Shipping &amp; Terms</li><li>Create an Account</li><li>Cart</li></ul>
  </div>
  <div class="footer-col newsletter" style="left:803px">
    <h4>JOIN OUR NEWSLETTER</h4>
    <p>Lorem ipsum dolor sit amet, clorons ectetur adipiscing elo elius.</p>
    <div class="news-input">Name:</div>
    <div class="news-btn">SIGN UP</div>
  </div>
  <div class="footer-rule"></div>
  <div class="copyright">Copyright © 2024 All rights are reserved.</div>
</footer>

</body>
</html>
```